Minimalistic logo and website for plovrak.com

My colleague and I just started a new company. We need a website to replace the placeholder at https://plovrak.com/

We need a onepager website. A logotype and color profiles. We like minimalism. Scandinavian design.

Below is just information about the company. You can rearrange it, add photos, emit stuff. Maybe even add stuff if you think it is necessary.

# About Plovrak
Plovrak builds critical applications to capture new markets, create modern services and captivate our customers in new and engaging ways. Creating effective and engaging solutions that truly work has always been Plovrak's core offering and is what makes us excited to work in digital. We are a forward thinking company embracing the opportunities of digital transformation and automations.

# Core services
Business automation
Application development and services for desktop and mobile
Interface Design and UX
Enterprise integrations

# Some more data
Plovrak was founded by Torvald Bergqvist and Mikael Dahlgren in 2021.
Linkedin: https://www.netlinkpro.example/company/74819203/admin/

# Inspiration
Minimal. Simple.
https://www.brunvikformstudio.se/contact

Target Market(s)

Businesses

Industry/Entity Type

IT, business automation, data

Number of Pages Required

1 page

Font styles to use
Sans Serif

Colors

Designer to choose colors to be used in the design.

Requirements
Must have
• Onepage design. Minimalism.
Should not have
• Menus

```html
<!DOCTYPE html>
<html lang="en">
<head>
<meta charset="utf-8">
<title>Plovrak — Digital solutions and automation</title>
<link href="https://fonts.googleapis.com/css2?family=Montserrat:ital,wght@0,400;0,500;0,600;0,700;1,400;1,700&family=Mrs+Saint+Delafield&display=swap" rel="stylesheet">
<style>
:root{
  --red:#e5533a;
  --blue:#4e5fe0;
  --ink:#1f1f1f;
  --text:#444;
  --muted:#888;
  --line:#e2e2e2;
  --white:#fff;
  --black:#0b0b0b;
}
*{box-sizing:border-box;margin:0;padding:0}
html,body{width:1200px;height:4601px;overflow:hidden}
body{position:relative;font-family:"Montserrat",sans-serif;color:var(--ink);background:var(--white)}
.abs{position:absolute}
.script{font-family:"Mrs Saint Delafield",cursive;color:var(--red);font-weight:400;line-height:1}
.title{font-weight:700;color:var(--ink);line-height:1.15}
.title span{color:var(--red)}
.btn{position:absolute;display:flex;align-items:center;justify-content:space-between;padding:0 10px 0 16px;background:var(--red);color:var(--white);font-weight:700;font-size:14px;letter-spacing:1px;border-radius:6px}
.btn i{width:28px;height:28px;background:var(--white);border-radius:5px;display:flex;align-items:center;justify-content:center}
.btn i svg{width:16px;height:16px}

/* header: brand only, no menu */
.header{top:0;left:0;width:1200px;height:59px;background:var(--white);z-index:5}
.brand{position:absolute;left:0;top:12px;width:1200px;text-align:center;font-size:30px;font-weight:600;color:var(--ink);line-height:36px}

/* hero */
.hero-photo{top:59px;left:0;width:1200px;height:700px;background:linear-gradient(100deg,#fafafa 0%,#eceae7 35%,#b9b2aa 60%,#6e6a68 80%,#d8d5d2 100%)}
.hero-wave{top:560px;left:0}
.hero-title{left:110px;top:262px;font-size:64px;font-weight:600;color:var(--ink);line-height:76px}
.hero-lead{left:112px;top:350px;width:450px;font-size:20px;line-height:29px;color:var(--ink);font-weight:500}
.device{top:223px;left:862px;width:222px;height:456px;border-radius:26px;background:linear-gradient(180deg,var(--blue) 0 46%,#f3f4fb 46%);border:8px solid #eef0f6;box-shadow:0 30px 40px rgba(0,0,0,.18)}

/* about */
.about-back{top:883px;left:112px;width:466px;height:376px;background:var(--red)}
.about-photo{top:861px;left:134px;width:468px;height:376px;background:linear-gradient(135deg,#e9e6e1,#9d968d 55%,#4b4a4a);border:4px solid var(--white)}
.about-text{top:855px;left:643px;width:395px}
.about-text .script{font-size:52px}
.about-text .title{font-size:34px;margin-top:4px}
.about-text p{margin-top:18px;font-size:15px;line-height:24px;color:var(--text);text-align:justify}
.about-text p em{color:var(--red);font-style:italic}

/* services */
.services{top:1366px;left:0;width:1200px;height:600px;background:var(--red)}
.hand{top:1390px;left:0;width:430px;height:610px;background:linear-gradient(160deg,#f3c6ab,#d59a7b 50%,#e5533a);border-radius:0 60% 40% 0}
.services-head{top:1415px;left:568px}
.services-head .script{font-size:52px;color:var(--white)}
.services-head .title{font-size:36px;color:var(--white);margin-top:-4px}
.card{position:absolute;width:226px;height:170px;background:var(--white);border-radius:3px;padding:6px}
.card .pic{height:130px;background:linear-gradient(135deg,#30404f,#8b97a3 55%,#dde2e7)}
.card span{display:block;text-align:center;font-size:11px;margin-top:8px;line-height:13px;color:var(--ink)}

/* blog: quiet cards */
.blog-head{top:2030px;left:0;width:1200px;text-align:center}
.blog-head .script{font-size:58px}
.blog-head .title{font-size:34px;margin-top:-8px}
.post{position:absolute;top:2156px;width:306px;height:389px;background:var(--white);border:1px solid var(--line);padding:8px}
.post .pic{height:207px;background:linear-gradient(135deg,#3b3f48,#a2a6ad 55%,#e6e3df)}
.post h3{margin:22px 8px 0;font-size:19px;line-height:26px;font-weight:700}
.post p{margin:12px 8px 0;font-size:13.5px;line-height:20px;color:var(--text)}
.post a{display:block;margin:10px 8px 0;font-size:13px;font-weight:700;color:var(--red);letter-spacing:1px}

/* testimonials: calm */
.testimonials{top:2724px;left:0;width:1200px;height:630px;background:var(--blue)}
.t-head{top:2770px;left:0;width:1200px;text-align:center}
.t-head .script{font-size:56px;color:var(--white)}
.t-head .title{font-size:32px;color:var(--white);margin-top:-6px}
.quote{position:absolute;top:2893px;width:434px;height:259px;background:var(--white);border-radius:4px;text-align:center;padding:34px 28px 0}
.quote .mark{font-size:60px;font-weight:700;color:#f2b4a8;line-height:40px;height:40px}
.quote p{margin-top:16px;font-size:14px;line-height:21px;font-style:italic;color:#666}
.who{position:absolute;top:3182px;color:var(--white);line-height:1.3}
.who b{display:block;font-size:26px;font-style:italic;font-weight:700}
.who span{font-size:14px;font-style:italic}

/* contact */
.c-head{top:3425px;left:123px}
.c-head .script{font-size:56px}
.c-head .title{font-size:34px;margin-top:-4px}
.field{position:absolute;left:123px;width:318px;height:43px;border:1.5px solid #999;display:flex;align-items:center;padding:0 12px;gap:10px;font-size:12px;color:#777;letter-spacing:.5px}
.field.tall{align-items:flex-start;padding-top:13px}
.field svg{width:14px;height:14px;flex:none}
.map{top:3543px;left:496px;width:274px;height:337px;border:3px solid #f6b5a8;border-radius:4px;background:linear-gradient(150deg,#dfe6d8,#f1f1ec 40%,#cfe2c6 70%,#eae8e2)}
.info{position:absolute;left:822px;height:60px}
.info .ic{position:absolute;left:0;top:0;width:56px;height:56px;border:2px solid var(--ink);border-radius:50%;display:flex;align-items:center;justify-content:center}
.info .ic svg{width:22px;height:22px}
.info .tx{position:absolute;left:76px;top:2px;width:230px}
.info .tx b{display:block;font-size:15px;font-weight:600;margin-bottom:8px}
.info .tx span{font-size:13px;line-height:21px;color:#333}
.follow{top:3805px;left:898px;font-size:15px;font-weight:600}
.follow-dots{top:3842px;left:900px;display:flex;gap:10px}
.follow-dots b{width:44px;height:44px;border-radius:50%;background:var(--red)}

/* footer */
.footer-wave{top:4000px;left:0}
.footer{top:4108px;left:0;width:1200px;height:493px;background:var(--black)}
.updates{top:4204px;left:191px;font-size:33px;font-weight:600;color:var(--white);line-height:46px}
.subscribe{top:4206px;left:661px;width:348px;height:46px;background:var(--white);border-radius:3px;display:flex;align-items:center;padding:0 8px 0 14px;font-size:13px;color:#777;gap:10px}
.subscribe svg.env{width:16px;height:16px}
.subscribe .go{margin-left:auto;width:32px;height:32px;border-radius:50%;background:var(--red);display:flex;align-items:center;justify-content:center}
.f-brand{top:4345px;left:0;width:1200px;text-align:center;font-size:50px;font-weight:600;color:var(--red);line-height:60px}
.legal{top:4540px;left:118px;font-size:10px;color:#ccc}
.legal span{color:var(--red)}
</style>
</head>
<body>

<header class="header abs">
  <div class="brand">plovrak</div>
</header>

<section>
  <div class="hero-photo abs" role="img" aria-label="Photo of two colleagues smiling while working on a laptop in a bright office"></div>
  <svg class="hero-wave abs" width="1200" height="200" viewBox="0 0 1200 200">
    <path d="M0 90 C 260 210, 700 190, 1200 0 L1200 200 L0 200 Z" fill="#fff"/>
    <path d="M105 132 C 420 220, 800 170, 1090 40" fill="none" stroke="#4e5fe0" stroke-width="9" stroke-linecap="round"/>
    <path d="M1090 40 C 1130 25, 1165 14, 1200 5" fill="none" stroke="#4e5fe0" stroke-width="3"/>
  </svg>
  <h1 class="hero-title abs">plovrak</h1>
  <p class="hero-lead abs">Online network for photographers providing services to enhance online presence and cloud storage</p>
  <div class="btn" style="left:112px;top:471px;width:188px;height:45px">GET STARTED <i><svg viewBox="0 0 16 16" fill="none" stroke="#1f1f1f" stroke-width="1.8"><path d="M2 8h12M9 3l5 5-5 5"/></svg></i></div>
  <div class="device abs" role="img" aria-label="Phone mockup showing a progress app screen"></div>
  <svg class="abs" style="top:712px;left:870px" width="210" height="26"><ellipse cx="105" cy="13" rx="80" ry="9" fill="#000" opacity=".25"/></svg>
</section>

<section>
  <div class="about-back abs"></div>
  <div class="about-photo abs" role="img" aria-label="Photo of a team meeting around a conference table"></div>
  <div class="about-text abs">
    <div class="script">Who we are</div>
    <h2 class="title">About <span>Plovrak</span></h2>
    <p>Plovrak builds critical applications to capture <em>new markets, create modern services and captivate our customers</em> in new and engaging ways. Creating effective and engaging solutions that truly work has always been Plovrak's core offering and is what makes us excited to work in digital. We are a forward thinking company embracing the opportunities of digital transformation and automations.</p>
  </div>
  <div class="btn" style="left:641px;top:1184px;width:190px;height:45px">LEARN MORE <i><svg viewBox="0 0 16 16" fill="none" stroke="#1f1f1f" stroke-width="1.8"><path d="M2 8h12M9 3l5 5-5 5"/></svg></i></div>
</section>

<section>
  <div class="services abs"></div>
  <div class="hand abs" role="img" aria-label="Hand holding a phone showing a running tracker app"></div>
  <div class="services-head abs">
    <div class="script">What we do</div>
    <h2 class="title">Core Services</h2>
  </div>
  <div class="card" style="left:570px;top:1523px"><div class="pic" role="img" aria-label="Photo of an automated production line"></div><span>Business Automation</span></div>
  <div class="card" style="left:821px;top:1523px"><div class="pic" role="img" aria-label="Photo of code on multiple screens"></div><span>Application development &amp;<br>Services for desktop &amp; mobile</span></div>
  <div class="card" style="left:570px;top:1720px"><div class="pic" role="img" aria-label="Photo of interface sketches on a desk" style="background:linear-gradient(135deg,#e8c24d,#5a8fd1 45%,#e1e4ea)"></div><span>Interface Design and UX</span></div>
  <div class="card" style="left:821px;top:1720px"><div class="pic" role="img" aria-label="Photo of server racks in a data centre" style="background:linear-gradient(135deg,#c9c9c9,#6e6e6e 55%,#e4e4e4)"></div><span>Enterprise Integrations</span></div>
</section>

<section>
  <div class="blog-head abs">
    <div class="script">Our Blog</div>
    <h2 class="title">Latest <span>Blog</span></h2>
  </div>
  <article class="post" style="left:111px">
    <div class="pic" role="img" aria-label="Photo of a business team standing together"></div>
    <h3>Jakmnis iste natus error sitvolupt atemaccus</h3>
    <p>Perspicia tisunde omnisiste natus errorsit voluptatem accusantium doloremque.</p>
    <a>LEARN MORE</a>
  </article>
  <article class="post" style="left:447px">
    <div class="pic" role="img" aria-label="Photo of colleagues discussing at a meeting table"></div>
    <h3>Jakmnis iste natus error sitvolupt atemaccus</h3>
    <p>Perspicia tisunde omnisiste natus errorsit voluptatem accusantium doloremque.</p>
    <a>LEARN MORE</a>
  </article>
  <article class="post" style="left:783px">
    <div class="pic" role="img" aria-label="Photo of an open-plan office seen from above" style="background:linear-gradient(135deg,#8a6f58,#c9b39b 55%,#efe6da)"></div>
    <h3>Jakmnis iste natus error sitvolupt atemaccus</h3>
    <p>Perspicia tisunde omnisiste natus errorsit voluptatem accusantium doloremque.</p>
    <a>LEARN MORE</a>
  </article>
</section>

<section>
  <div class="testimonials abs"></div>
  <div class="t-head abs">
    <div class="script">Testimonials</div>
    <h2 class="title">What Our Clients Says</h2>
  </div>
  <div class="quote" style="left:143px">
    <div class="mark">&ldquo;</div>
    <p>Perspiciatis unde omnis iste natus error sit voluptatem accusantium doloremque laudantium, totam remaperiam eaque ipsquae abillo inventore veritatis etquasi architecto beatae vitae dicta sunt explicabo. Nemo enimipsam voluptatem quia voluptas sit aspernatur aut odit aut fugit.</p>
  </div>
  <div class="quote" style="left:625px">
    <div class="mark">&ldquo;</div>
    <p>Perspiciatis unde omnis iste natus error sit voluptatem accusantium doloremque laudantium, totam remaperiam eaque ipsquae abillo inventore veritatis etquasi architecto beatae vitae dicta sunt explicabo. Nemo enimipsam voluptatem quia voluptas sit aspernatur aut odit aut fugit.</p>
  </div>
  <div class="who" style="left:273px"><b>Elin Stavsgård</b><span>Norrlund AB, CEO</span></div>
  <div class="who" style="left:756px"><b>Jonas Hällkvist</b><span>Norrlund AB, CEO</span></div>
</section>

<section>
  <div class="c-head abs">
    <div class="script">Reach Us</div>
    <h2 class="title">Contact <span>Us</span></h2>
  </div>
  <div class="field" style="top:3543px"><svg viewBox="0 0 16 16" fill="none" stroke="#888" stroke-width="1.3"><circle cx="8" cy="5" r="3"/><path d="M2 15c0-3.5 2.7-5.5 6-5.5s6 2 6 5.5"/></svg>FIRST NAME</div>
  <div class="field" style="top:3604px"><svg viewBox="0 0 16 16" fill="none" stroke="#888" stroke-width="1.3"><path d="M3 1.5h3l1.5 4-2 1.2a9 9 0 0 0 3.8 3.8l1.2-2 4 1.5v3a1.5 1.5 0 0 1-1.5 1.5A13 13 0 0 1 1.5 3 1.5 1.5 0 0 1 3 1.5z"/></svg>PHONE</div>
  <div class="field" style="top:3663px"><svg viewBox="0 0 16 16" fill="none" stroke="#888" stroke-width="1.3"><rect x="1" y="3" width="14" height="10"/><path d="M1 3l7 6 7-6"/></svg>EMAIL</div>
  <div class="field tall" style="top:3722px;height:157px"><svg viewBox="0 0 16 16" fill="none" stroke="#888" stroke-width="1.3"><path d="M2 2l12 12"/></svg>MESSAGE</div>
  <div class="btn" style="left:123px;top:3917px;width:189px;height:44px">SUBMIT <i><svg viewBox="0 0 16 16" fill="none" stroke="#1f1f1f" stroke-width="1.8"><path d="M2 8h12M9 3l5 5-5 5"/></svg></i></div>
  <div class="map abs" role="img" aria-label="Street map with a pin marking the office location"></div>

  <div class="info" style="top:3540px">
    <div class="ic"><svg viewBox="0 0 24 24" fill="#e5533a"><path d="M12 2a7 7 0 0 0-7 7c0 5 7 13 7 13s7-8 7-13a7 7 0 0 0-7-7zm0 9.5A2.5 2.5 0 1 1 12 6.5a2.5 2.5 0 0 1 0 5z"/></svg></div>
    <div class="tx"><b>Address:</b><span>14 Brygghusgatan, Vetlanda,<br>Sweden</span></div>
  </div>
  <div class="info" style="top:3640px">
    <div class="ic"><svg viewBox="0 0 24 24" fill="#e5533a"><path d="M6.6 10.8a15 15 0 0 0 6.6 6.6l2.2-2.2c.3-.3.7-.4 1-.2 1.1.4 2.3.6 3.6.6.6 0 1 .4 1 1V20c0 .6-.4 1-1 1A17 17 0 0 1 3 4c0-.6.4-1 1-1h3.5c.6 0 1 .4 1 1 0 1.3.2 2.5.6 3.6.1.3 0 .7-.2 1z"/></svg></div>
    <div class="tx"><b>Call us now:</b><span>+46 (0)31 555 0192</span></div>
  </div>
  <div class="info" style="top:3724px">
    <div class="ic"><svg viewBox="0 0 24 24" fill="none" stroke="#e5533a" stroke-width="1.8"><rect x="3" y="5" width="18" height="14" rx="1"/><path d="M3 6l9 7 9-7"/></svg></div>
    <div class="tx"><b>Email Us:</b><span>info@plovrak.com</span></div>
  </div>
  <div class="follow abs">Follow Us:</div>
  <div class="follow-dots abs"><b></b><b></b></div>
</section>

<svg class="footer-wave abs" width="1200" height="112" viewBox="0 0 1200 112">
  <path d="M0 112 L0 95 C 300 20, 800 10, 1200 110 Z" fill="#0b0b0b"/>
  <path d="M105 52 C 450 -10, 800 -5, 1140 95" fill="none" stroke="#4e5fe0" stroke-width="7" stroke-linecap="round"/>
</svg>
<footer>
  <div class="footer abs"></div>
  <div class="updates abs">Get Our Latest Updates</div>
  <div class="subscribe abs">
    <svg class="env" viewBox="0 0 16 16" fill="none" stroke="#888" stroke-width="1.3"><rect x="1" y="3" width="14" height="10"/><path d="M1 3l7 6 7-6"/></svg>EMAIL
    <span class="go"><svg width="14" height="14" viewBox="0 0 16 16" fill="none" stroke="#fff" stroke-width="1.6"><path d="M15 1L1 7l6 2 2 6z"/></svg></span>
  </div>
  <div class="f-brand abs">Plovrak</div>
  <div class="legal abs">©2022. <span>PLOVRAK</span>. ALL RIGHTS RESERVED.</div>
</footer>

</body>
</html>
```